Criação de Apres. Comercial (com dobra) para Brisa & Horizonte
" O departamento de medicina do trabalho realiza exames nos funcionários das empresas, em nossa Central de Atendimento e também nas empresas. O departamento de segurança do trabalho visita as empresas para elaborar laudos e outros documentos legais. Outros trabalhos, tais como treinamentos e assessoria trabalhista, também são realizados "

```html
<!DOCTYPE html>
<html lang="pt-BR">
<head>
<meta charset="utf-8">
<title>Brisa &amp; Horizonte — Quem Somos</title>
<link rel="stylesheet" href="https://fonts.googleapis.com/css2?family=Oswald:wght@500;600&family=Open+Sans:wght@400;700;800&display=swap">
<style>
  :root {
    --bg: #e9e9e9;
    --paper: #ffffff;
    --red: #c8202e;
    --ink: #4a4a4a;
    --ink-strong: #222222;
    --photo-top: #e6ebef;
    --photo-bottom: #c3ced7;
    --disc-ring: #c9ced3;
  }
  * { box-sizing: border-box; margin: 0; padding: 0; }
  html, body { width: 1200px; height: 1200px; overflow: hidden; }
  body {
    background: var(--bg);
    font-family: "Open Sans", Arial, sans-serif;
    color: var(--ink);
    position: relative;
  }
  .spread {
    position: absolute;
    left: 36px; top: 150px;
    width: 1128px; height: 900px;
    display: flex;
    box-shadow: 0 10px 30px rgba(0,0,0,.18);
  }
  .page {
    position: relative;
    width: 564px; height: 900px;
    background: var(--paper);
    overflow: hidden;
  }
  .page-number {
    position: absolute;
    bottom: 20px;
    font-family: "Oswald", sans-serif;
    font-weight: 500;
    font-size: 18px;
    color: var(--red);
  }
  .page--left .page-number { left: 24px; }
  .page--right .page-number { right: 24px; }

  /* Left page */
  .cover-photo {
    position: absolute; inset: 0;
    background: linear-gradient(160deg, var(--photo-top) 0%, var(--photo-bottom) 100%);
  }
  .brand-disc {
    position: absolute;
    left: 238px; top: 238px;
    width: 220px; height: 220px;
    border-radius: 50%;
    background: var(--paper);
    border: 10px solid var(--disc-ring);
    display: flex; align-items: center; justify-content: center;
    text-align: center;
  }
  .brand-name {
    font-family: "Open Sans", sans-serif;
    font-weight: 800;
    font-size: 25px;
    line-height: 1.15;
    color: var(--red);
  }

  /* Right page */
  .title-bar {
    position: absolute;
    right: 0; top: 22px;
    width: 14px; height: 210px;
    background: var(--red);
  }
  .title {
    position: absolute;
    right: 40px; top: 30px;
    text-align: right;
    font-family: "Oswald", sans-serif;
    font-weight: 600;
    font-size: 92px;
    line-height: 1;
    letter-spacing: 3px;
    color: var(--red);
  }
  .intro {
    position: absolute;
    left: 60px; right: 40px; top: 290px;
    font-size: 14px; line-height: 1.55;
    text-align: justify;
    text-indent: 5em;
  }
  .intro strong { color: var(--ink-strong); font-weight: 800; }
  .benefits {
    position: absolute;
    left: 40px; right: 30px; top: 395px;
    display: flex; justify-content: space-between;
  }
  .benefit {
    width: 150px;
    display: flex; flex-direction: column; align-items: center;
    text-align: center;
  }
  .benefit-icon { width: 72px; height: 80px; }
  .benefit-caption {
    margin-top: 10px;
    font-size: 8.5px; line-height: 1.35;
    font-weight: 800;
    color: var(--red);
    text-transform: uppercase;
  }
  .body-copy {
    position: absolute;
    left: 40px; right: 40px; top: 590px;
    font-size: 13.5px; line-height: 1.6;
    text-align: justify;
  }
  .body-copy p { text-indent: 2.5em; margin-bottom: 14px; }
  .body-copy strong { color: var(--ink-strong); font-weight: 800; }
</style>
</head>
<body>
  <div class="spread">
    <section class="page page--left">
      <div class="cover-photo" role="img" aria-label="Foto de um médico estendendo um estetoscópio em primeiro plano"></div>
      <div class="brand-disc">
        <span class="brand-name">Brisa &amp;<br>Horizonte</span>
      </div>
      <span class="page-number">02</span>
    </section>

    <section class="page page--right">
      <div class="title-bar"></div>
      <h1 class="title">QUEM<br>SOMOS</h1>

      <p class="intro">Desde 1988 acompanhando o dia-a-dia de mais de <strong>4.600 clientes</strong> e <strong>280.000 vidas</strong>, com satisfação afirmamos que nosso trabalho tem atingido objetivos importantes, tais como:</p>

      <div class="benefits">
        <div class="benefit">
          <svg class="benefit-icon" viewBox="0 0 72 80" aria-hidden="true">
            <polygon points="36,2 70,21 70,59 36,78 2,59 2,21" fill="var(--red)"/>
            <path d="M20 28 h24 a4 4 0 0 1 4 4 v12 a4 4 0 0 1 -4 4 h-14 l-7 6 v-6 h-3 a4 4 0 0 1 -4 -4 v-12 a4 4 0 0 1 4 -4z" fill="none" stroke="#fff" stroke-width="2.5"/>
            <circle cx="26" cy="38" r="2" fill="#fff"/><circle cx="32" cy="38" r="2" fill="#fff"/><circle cx="38" cy="38" r="2" fill="#fff"/>
          </svg>
          <p class="benefit-caption">Redução acentuada nas perdas por reclamações trabalhistas</p>
        </div>
        <div class="benefit">
          <svg class="benefit-icon" viewBox="0 0 72 80" aria-hidden="true">
            <polygon points="36,2 70,21 70,59 36,78 2,59 2,21" fill="var(--red)"/>
            <circle cx="36" cy="30" r="7" fill="none" stroke="#fff" stroke-width="2.5"/>
            <path d="M22 56 v-6 a14 12 0 0 1 28 0 v6z" fill="none" stroke="#fff" stroke-width="2.5"/>
            <path d="M30 48 l12 6" stroke="#fff" stroke-width="2.5"/>
          </svg>
          <p class="benefit-caption">Sensível diminuição na ocorrência de acidentes durante a jornada de trabalho</p>
        </div>
        <div class="benefit">
          <svg class="benefit-icon" viewBox="0 0 72 80" aria-hidden="true">
            <polygon points="36,2 70,21 70,59 36,78 2,59 2,21" fill="var(--red)"/>
            <path d="M24 22 h18 l8 8 v28 h-26z" fill="none" stroke="#fff" stroke-width="2.5"/>
            <path d="M29 32 h10 M29 38 h8" stroke="#fff" stroke-width="2"/>
            <text x="42" y="54" font-family="Open Sans, sans-serif" font-weight="800" font-size="14" fill="#fff" text-anchor="middle">$</text>
          </svg>
          <p class="benefit-caption">Eliminação de multas relativas à segurança e medicina do trabalho, contribuindo de forma direta para uma melhor condição</p>
        </div>
      </div>

      <div class="body-copy">
        <p>Oferecemos à sua empresa uma solução definitiva em Medicina e Segurança do Trabalho, através de nossa equipe de profissionais com larga experiência e uma estrutura adequada. Nossa Central de Atendimento oferece um excelente suporte englobando a realização de <strong>exames clínicos</strong>, <strong>audiométricos</strong>, de <strong>acuidade visual</strong>, <strong>ECG</strong>, <strong>EEG</strong>, <strong>espirometria</strong> e <strong>coleta de análises clínicas</strong>, além de um plantão de dúvidas formado por engenheiros e médicos do trabalho que está à disposição dos clientes para auxiliá-los no que for preciso, respeitando suas prioridades.</p>
        <p>Nossa Coordenação de Operações tem controle absoluto dos contratos, levando à sua empresa confiabilidade e segurança.</p>
      </div>

      <span class="page-number">03</span>
    </section>
  </div>
</body>
</html>
```